Webdesign for starlight path

"Der Sternpfad" is a new info product that will be selled through the website maybe you will create for us.

Translated from german to english the project is named "the starlight path". It´s an online video course that teaches people how to live a fulfilling, happy and healthy life.

Design paramaters
We want a serious design that embodies the real feeling of beeing happy and fulfilled. Visitors should even feel good/better when they see the website.
In color psychology some sort of calming deep green like a four-leaf clover is recommend.
Mainly the website will be the external sales page with a big video as the central attention.
We also need a member area for customers to watch our video course.

So mainly we need a eye-cathing, calming header, the content body with mainly video and just a few written words...and of course a footer for links like imprint, affiliate program etc.

What we not want:
- some kind of these exaggerated smiling photos
- that bathetic luck symbols like money or boats

Hi,

i posted a message to the design discussion. Thank you!

```html
<!DOCTYPE html>
<html lang="en">
<head>
<meta charset="utf-8">
<title>Starlight Path</title>
<link href="https://fonts.googleapis.com/css2?family=Cinzel:wght@400;700&family=Source+Sans+3:wght@400;600&family=Arimo:ital,wght@0,400;1,400&display=swap" rel="stylesheet">
<style>
:root{
  --lime:#a3c545;
  --lime-edge:#3aa6a0;
  --forest:#6b8a22;
  --ink:#0d0d0d;
  --panel:#222222;
  --panel-text:#d2d2d2;
  --accent:#1d8fd6;
  --logo:#d6e48a;
  --link:#7fc7ec;
  --field:#d5f3dc;
  --grey:#bdbdbd;
  --white:#ffffff;
}
*{margin:0;padding:0;box-sizing:border-box}
html,body{width:900px;height:1200px;overflow:hidden}
body{position:relative;background:var(--white);font-family:'Arimo',Arial,sans-serif}
.abs{position:absolute}

/* header */
.header{left:0;top:0;width:900px;height:336px;background:var(--lime);border:1px solid var(--lime-edge);border-top:5px solid #2f3a12}
.header-shadow{left:0;top:336px;width:900px;height:16px;background:linear-gradient(#111,#3a3a3a 60%,#111)}
.stage{left:0;top:352px;width:900px;height:423px;background:linear-gradient(#e4e4e4,#fff 12%,#fff 80%,#ececec)}
.logo{left:87px;top:0;width:227px;height:62px;background:var(--ink);display:flex;align-items:center;justify-content:center;font-family:'Cinzel',serif;font-size:25px;color:var(--logo);letter-spacing:.5px}
.feedback{left:683px;top:0;width:126px;height:36px;background:linear-gradient(#3a3a3a,#0e0e0e);border-radius:0 0 4px 4px;color:var(--white);font-family:'Source Sans 3',sans-serif;font-size:17px;padding:10px 0 0 20px;box-shadow:0 4px 6px rgba(0,0,0,.35)}
.feedback svg{position:absolute;right:10px;top:15px}

/* nav */
.nav{left:90px;top:95px;width:720px;height:32px;background:linear-gradient(#3b3b3b,#090909);border-top:2px solid #111;display:flex;align-items:center;padding-left:12px}
.nav a{font-family:'Cinzel',serif;font-size:11.5px;color:#d8d8d8;text-decoration:none;letter-spacing:.6px;padding:0 13px;border-right:1px solid #555;line-height:16px}
.nav a.current{background:linear-gradient(#3fb0e0,#0f6f9e);color:var(--white);border-radius:10px;padding:2px 10px;border:none;margin-right:0}
.nav a:last-of-type{border:none}
.search{left:668px;top:100px;width:134px;height:21px;background:linear-gradient(#9a9a9a,#6c6c6c);border-radius:5px;color:var(--white);font-size:12px;padding:4px 11px}
.search-btn{left:760px;top:98px;width:33px;height:26px;background:linear-gradient(#2aa4f0,#0b62b4);border-radius:4px}

/* video */
.video-panel{left:90px;top:150px;width:720px;height:311px;background:var(--panel);border:3px solid #000;box-shadow:0 8px 10px -4px rgba(0,0,0,.5)}
.video-frame{left:100px;top:161px;width:414px;height:289px;background:linear-gradient(#dfe9f2 0%,#c6d7a8 20%,#8ea83a 30%,#6f8f22 60%,#4b6a18 100%)}
.play{left:265px;top:255px}
.video-info{left:525px;top:152px;width:280px;color:var(--panel-text);font-family:'Source Sans 3',sans-serif;font-size:17.4px;line-height:21.8px}
.video-info h2{font-family:'Cinzel',serif;font-weight:400;font-size:19px;text-align:center;letter-spacing:1px;margin:3px 0 12px;color:#c8c8c8}
.video-info .indent{padding-left:93px}
.video-info .cat{margin-top:32px}
.video-info .cat-value{padding-left:74px}
.arrow{top:292px}

/* thumbnails */
.thumb{top:515px;width:135px}
.thumb .pic{height:128px;background:#0c0c0c;border-radius:3px;padding:8px 5px 8px 5px}
.thumb .pic div{height:100%}
.sunset{background:linear-gradient(160deg,#e0503a,#f0a030 55%,#8a7a2a)}
.sea{background:linear-gradient(#3d67b0,#22478e 60%,#1b3b78)}
.thumb p{font-size:10px;line-height:14px;color:#222;margin:8px 0 0 1px}
.thumb .btn{margin-top:10px;height:31px;background:linear-gradient(#4a4a4a,#0c0c0c);border-radius:4px;color:var(--white);font-family:'Source Sans 3',sans-serif;font-size:20px;text-align:center;line-height:30px;box-shadow:0 9px 8px -6px rgba(0,0,0,.45)}

/* footer */
.band{left:0;top:775px;width:900px;height:26px;background:linear-gradient(#4a4a4a,#0c0c0c)}
.footer{left:0;top:801px;width:900px;height:334px;background:var(--forest)}
.footer h3{position:absolute;font-weight:400;font-size:17.5px;color:var(--white)}
.post{left:90px;width:232px;display:flex;gap:16px;border-bottom:1px dotted #8fad44;padding-bottom:6px}
.post .pic{width:69px;height:64px;border:2px solid #fff;flex:none}
.post h4{font-weight:400;font-size:12px;color:var(--link);margin-top:3px}
.post p{font-size:11px;line-height:13px;color:var(--white);margin-top:3px}
.social{top:869px;width:33px;height:33px;border-radius:7px;background:#55701a;border:2px solid #8aa63a}
.contact{left:377px;font-size:12px;color:var(--white);display:flex;gap:10px}
.contact em{color:var(--link)}
.field{left:621px;width:143px;height:29px;background:var(--field);border:1px solid #3a5a12}
.field-label{left:779px;font-size:11px;color:var(--white)}
.submit{left:740px;top:1046px;width:67px;height:23px;background:linear-gradient(#3a3a3a,#0d1a08);border-radius:3px;color:var(--white);font-size:11px;text-align:center;line-height:22px}

.bottom{left:0;top:1135px;width:900px;height:65px;background:linear-gradient(#d9d9d9,#a9a9a9)}
.bottom-line{left:0;top:1158px;width:900px;height:16px;background:#111}
.bottom-bar{left:90px;top:1143px;width:734px;height:41px;background:linear-gradient(#3a3a3a,#0c0c0c);border-radius:3px;display:flex;align-items:center;padding:0 14px;box-shadow:0 4px 6px rgba(0,0,0,.4)}
.bottom-bar a{font-size:9.5px;color:var(--white);text-decoration:none;margin-right:22px}
.bottom-bar span{margin-left:auto;font-size:9.5px;color:var(--white)}
</style>
</head>
<body>

<header>
  <div class="abs header"></div>
  <div class="abs logo">Starlight Path</div>
  <div class="abs feedback">Feedback
    <svg width="6" height="9" viewBox="0 0 6 9"><path d="M0 0L6 4.5L0 9Z" fill="#2aa4f0"/></svg>
  </div>
  <nav class="abs nav">
    <a class="current" href="#">Home</a>
    <a href="#" style="margin-left:10px">Services</a>
    <a href="#">Courses</a>
    <a href="#">Products</a>
    <a href="#">About</a>
    <a href="#">Blog</a>
    <a href="#">Contact</a>
  </nav>
  <div class="abs search">search</div>
  <div class="abs search-btn">
    <svg width="33" height="26" viewBox="0 0 33 26"><circle cx="15" cy="12" r="6" fill="none" stroke="#fff" stroke-width="2.5"/><path d="M19.5 16.5L24 21" stroke="#fff" stroke-width="3" stroke-linecap="round"/></svg>
  </div>
</header>

<div class="abs header-shadow"></div>
<div class="abs stage"></div>

<main>
  <section class="abs video-panel"></section>
  <div class="abs video-frame" role="img" aria-label="Meadow of grass and yellow wildflowers under a pale sky"></div>
  <svg class="abs play" width="108" height="108" viewBox="0 0 108 108"><circle cx="54" cy="54" r="52" fill="rgba(255,255,255,.35)" stroke="rgba(255,255,255,.5)" stroke-width="2"/><path d="M38 30L82 54L38 78Z" fill="#111"/></svg>
  <div class="abs video-info">
    <h2>Video Name</h2>
    <p>Discription:-</p>
    <p class="indent">This is the dummy text-</p>
    <p>This is the dummy text This is the dummy text This is the dummy text This is the dummy text This is the dummy text This is the dummy text This is the dummy text This is the dummy text.</p>
    <p class="cat">Category:-</p>
    <p class="cat-value">Yoga and dummy text</p>
  </div>
  <svg class="abs arrow" style="left:66px" width="26" height="38" viewBox="0 0 26 38"><path d="M24 0L0 19L24 38Z" fill="#111"/><path d="M20 10L12 19L20 28" fill="none" stroke="#2aa4f0" stroke-width="2.5"/></svg>
  <svg class="abs arrow" style="left:808px" width="26" height="38" viewBox="0 0 26 38"><path d="M2 0L26 19L2 38Z" fill="#111"/><path d="M6 10L14 19L6 28" fill="none" stroke="#2aa4f0" stroke-width="2.5"/></svg>

  <article class="abs thumb" style="left:90px">
    <div class="pic"><div class="sunset" role="img" aria-label="Bare tree against an orange sunset"></div></div>
    <p>Neque porro quisquam est,<br>qui dolorem ipsum quia dolor.</p>
    <div class="btn">Video 2</div>
  </article>
  <article class="abs thumb" style="left:285px">
    <div class="pic"><div class="sea" role="img" aria-label="Dolphins leaping from blue water"></div></div>
    <p>Neque porro quisquam est,<br>qui dolorem ipsum quia dolor.</p>
    <div class="btn">Video 3</div>
  </article>
  <article class="abs thumb" style="left:480px">
    <div class="pic"><div class="sunset" role="img" aria-label="Bare tree against an orange sunset"></div></div>
    <p>Neque porro quisquam est,<br>qui dolorem ipsum quia dolor.</p>
    <div class="btn">Video 4</div>
  </article>
  <article class="abs thumb" style="left:675px">
    <div class="pic"><div class="sea" role="img" aria-label="Dolphins leaping from blue water"></div></div>
    <p>Neque porro quisquam est,<br>qui dolorem ipsum quia dolor.</p>
    <div class="btn">Video 5</div>
  </article>
</main>

<footer>
  <div class="abs band"></div>
  <div class="abs footer"></div>
  <div class="footer-content">
    <h3 style="left:90px;top:837px">Recent Posts</h3>
    <div class="abs post" style="top:872px">
      <div class="pic" style="background:linear-gradient(#b9302a,#efe6d8 40%,#c8a070)" role="img" aria-label="Website screenshot thumbnail"></div>
      <div><h4>This is the dummy text</h4><p>This is the dummy text This is the dummy text This is the dummy text.</p></div>
    </div>
    <div class="abs post" style="top:958px">
      <div class="pic sunset" role="img" aria-label="Bare tree against an orange sunset"></div>
      <div><h4>This is the dummy text</h4><p>This is the dummy text This is the dummy text This is the dummy text.</p></div>
    </div>
    <div class="abs post" style="top:1042px;border:none">
      <div class="pic" style="background:linear-gradient(#f4f4f4,#8ab04a 50%,#7a3a9a)" role="img" aria-label="Website screenshot thumbnail"></div>
      <div><h4>This is the dummy text</h4><p>This is the dummy textThis is the dummy textThis is the dummy textt....</p></div>
    </div>

    <h3 style="left:378px;top:837px">Keep Up With Us</h3>
    <div class="abs social" style="left:413px"></div>
    <div class="abs social" style="left:452px"></div>
    <div class="abs social" style="left:491px"></div>

    <h3 style="left:376px;top:949px">The Old Fashioned Way</h3>
    <div class="abs contact" style="top:984px">
      <svg width="12" height="12" viewBox="0 0 12 12"><rect x="1" y="3" width="10" height="8" rx="1" fill="#ddd"/><path d="M2 3Q6 0 10 3" fill="none" stroke="#ddd" stroke-width="1.5"/></svg>
      <span style="margin-left:7px">Phone:&nbsp; <em>555.014.2290</em></span>
    </div>
    <div class="abs contact" style="top:1009px">
      <svg width="12" height="12" viewBox="0 0 12 12"><rect x="0.5" y="2.5" width="11" height="7" fill="#eee"/><path d="M0.5 2.5L6 7L11.5 2.5" fill="none" stroke="#777"/></svg>
      <span style="margin-left:7px">Email:&nbsp; <em>hello@starlightpath.example</em></span>
    </div>
    <div class="abs contact" style="top:1034px">
      <svg width="14" height="14" viewBox="0 0 14 14"><path d="M1 7L7 1L13 7V13H1Z" fill="#eee"/><rect x="5.5" y="9" width="3" height="4" fill="#555"/></svg>
      <span style="margin-left:4px">Address:&nbsp; <em>48 Meadow Lane N.<br>&nbsp;&nbsp;&nbsp;&nbsp;&nbsp;&nbsp;&nbsp;&nbsp;&nbsp;&nbsp;&nbsp;&nbsp;&nbsp;&nbsp;&nbsp;&nbsp;Brookfield, State 40112</em></span>
    </div>

    <h3 style="left:620px;top:836px">Reach Out To Us</h3>
    <div class="abs field" style="top:874px"></div>
    <div class="abs field-label" style="top:880px">name*</div>
    <div class="abs field" style="top:913px"></div>
    <div class="abs field-label" style="top:919px">email*</div>
    <div class="abs field" style="top:951px;width:187px;height:83px"></div>
    <div class="abs submit">Submit</div>
  </div>

  <div class="abs bottom"></div>
  <div class="abs bottom-line"></div>
  <nav class="abs bottom-bar">
    <a href="#">Home</a><a href="#">Services</a><a href="#">Courses</a><a href="#">Products</a><a href="#">About</a><a href="#">Blog</a><a href="#">Contact</a>
    <span>© 2012 All Rights Reserved Starlight Path</span>
  </nav>
</footer>

</body>
</html>
```